pressure washing advertisment

I would like front and back designed post cards. we offer pressure washing services for residential customers. I want to highlight before and after pictures as examples of our more popular services. I would also like to have our email www.brightlanewashco.com and the facebook and Instagram logo somewhere. you can also include all major credit card logos as acceptable payments. I have attached our logo along with before and after pictures. also feel free to go to my website for any additional information that should be added to the post card. lastly I want a small promotion of $25 off any service somewhere.<br/><br/>Thank you!!

Target Market(s)

homeowners

Industry/Entity Type

Cleaning Service

Font styles to use
Serif
Sans Serif

Colors

Designer to choose colors to be used in the design.

Requirements
Must have
• before and after pictures with website and logo
Nice to have
• clean look that flows

```html
<!DOCTYPE html>
<html lang="en">
<head>
<meta charset="utf-8">
<title>Brightlane Wash Co. Postcard</title>
<link href="https://fonts.googleapis.com/css2?family=Crimson+Pro:wght@400;600;700&family=Lato:wght@400;700;800&family=Montserrat:wght@400&family=Oswald:wght@500&display=swap" rel="stylesheet">
<style>
  :root{
    --page:#9fb6c9;
    --navy:#0f3f7f;
    --navy-dark:#0c3468;
    --red:#e11d27;
    --label:#2d5c98;
    --sky:#5a8ee0;
    --ink:#222;
    --paper:#ffffff;
    --rule:#8a8f96;
  }
  *{margin:0;padding:0;box-sizing:border-box}
  html,body{width:800px;height:1200px;overflow:hidden;background:var(--page)}
  body{position:relative;font-family:"Lato",sans-serif;color:var(--ink)}
  .postcard{position:absolute;left:73px;width:656px;height:437px;background:var(--paper);overflow:hidden}
  .postcard--front{top:59px}
  .postcard--back{top:663px}
  .abs{position:absolute}

  /* front */
  .hero{left:9px;top:7px;width:395px;height:330px;
    background:
      radial-gradient(ellipse 90px 160px at 370px 210px,rgba(52,70,40,.85),rgba(52,70,40,0) 100%),
      linear-gradient(180deg,#5a8ee0 0%,#6d9de6 28%,#c9d6df 38%,#e8d79a 46%,#e1cb82 70%,#c7b06c 82%,#5f8440 92%,#4c6d34 100%)}
  .promo-ribbon{left:19px;top:7px;width:88px;height:96px}
  .promo-ribbon__text{left:19px;top:22px;width:88px;text-align:center;color:#fff}
  .promo-ribbon__amount{font-family:"Oswald",sans-serif;font-weight:500;font-size:34px;line-height:1}
  .promo-ribbon__amount small{font-family:"Lato",sans-serif;font-size:11px;font-weight:400}
  .promo-ribbon__sub{font-size:10px;letter-spacing:.2px;margin-top:3px}
  .headline{left:124px;top:16px;width:285px;font-family:"Crimson Pro",serif;font-weight:700;
    font-size:15.6px;line-height:17px;color:var(--navy-dark);letter-spacing:.3px}

  .result{width:116px;height:107px}
  .result__label{position:absolute;left:0;bottom:0;width:100%;height:24px;background:var(--label);
    color:#fff;font-family:"Crimson Pro",serif;font-size:17px;text-align:center;line-height:24px;letter-spacing:.6px}
  .result--siding{background:linear-gradient(160deg,#efe6c4 0%,#d9cd9c 55%,#cfc28c 100%)}
  .result--siding.dirty{background:linear-gradient(160deg,#ddd4ac 0%,#a9a27a 50%,#8d8a67 100%)}
  .result--drive{background:linear-gradient(180deg,#2f4a2c 0%,#4f6a3e 18%,#a9aaa4 30%,#bdbdb8 70%,#a3a39c 100%)}
  .result--drive.clean{background:linear-gradient(180deg,#2f4a2c 0%,#56763f 18%,#d7d7d2 30%,#e6e6e2 70%,#d8d8d3 100%)}
  .result--porch{background:linear-gradient(180deg,#c8ced6 0%,#7f8c93 35%,#9aa7ad 60%,#5d6b70 100%)}
  .result--porch.clean{background:linear-gradient(180deg,#eef2f6 0%,#aeb8bd 35%,#c1cace 60%,#7d8a8f 100%)}

  .brand{display:flex;align-items:center;gap:7px;font-family:"Lato",sans-serif;font-weight:800;color:var(--navy)}
  .brand__mark{background:var(--red)}
  .call-box{left:240px;top:344px;width:183px;height:36px}
  .call-box__top{height:17px;background:var(--navy);color:#fff;font-family:"Crimson Pro",serif;font-size:16px;text-align:center;line-height:18px;letter-spacing:.5px}
  .call-box__num{height:19px;background:var(--red);color:#fff;font-family:"Crimson Pro",serif;font-size:19px;text-align:center;line-height:19px;letter-spacing:.6px}
  .contact{display:flex;align-items:center;gap:6px;font-family:"Crimson Pro",serif;color:#333}
  .contact svg{flex:none}
  .pay-note{font-family:"Crimson Pro",serif;color:#333}
  .cards{display:flex;gap:2px}
  .card-chip{width:34px;height:22px;border-radius:3px;box-shadow:0 1px 2px rgba(0,0,0,.25)}
  .chip-a{background:linear-gradient(180deg,#fff,#e6e6e6)}
  .chip-b{background:linear-gradient(180deg,#2a86c9,#15609e)}
  .chip-c{background:linear-gradient(180deg,#5cb8ea,#2f92d0)}
  .chip-d{background:linear-gradient(180deg,#fff,#e9e9e9)}
  .social{display:flex;align-items:center;gap:4px;font-family:"Crimson Pro",serif;color:#333}
  .social__box{width:11px;height:11px;border-radius:2px}

  /* back */
  .service-photo{left:8px;top:7px;width:336px;height:141px;
    background:linear-gradient(90deg,#4a5560 0%,#8a939b 30%,#6f7a84 55%,#9aa7b0 75%,#7b9a6a 100%)}
  .service-band{left:8px;top:147px;width:336px;height:71px;background:var(--red)}
  .thumb{top:101px;width:79px;height:72px;border:1px solid #fff}
  .thumb--stain{background:linear-gradient(180deg,#e0d6c4 0%,#c47a3a 40%,#8a6a3a 52%,#5f8a3c 70%)}
  .thumb--wall{background:linear-gradient(180deg,#ecebe6 0%,#d3d2cb 45%,#7aa04a 65%,#5c8a36 100%)}
  .thumb--house{background:linear-gradient(180deg,#c7d3e0 0%,#5d626a 40%,#74787f 70%,#8e9299 100%)}
  .thumb--house.clean{background:linear-gradient(180deg,#c7d3e0 0%,#8e949c 40%,#c8cbcf 70%,#e0e2e4 100%)}
  .thumb__label{position:absolute;left:0;bottom:0;width:100%;height:16px;background:var(--label);color:#fff;
    font-family:"Crimson Pro",serif;font-size:12px;text-align:center;line-height:16px;letter-spacing:.3px}
  .service-title{left:8px;top:180px;width:336px;text-align:center;color:#fff;font-family:"Crimson Pro",serif;font-weight:400;font-size:15.5px;letter-spacing:.5px;line-height:18px}
  .service-sub{left:8px;top:198px;width:336px;text-align:center;color:#fff;font-family:"Crimson Pro",serif;font-size:9.2px}
  .services{left:0;top:218px;width:344px;height:162px;background:linear-gradient(180deg,#f4f5f8,#fbecec 60%,#f6f7fa)}
  .service__title{font-family:"Crimson Pro",serif;font-size:10.5px;line-height:11px;color:var(--navy)}
  .service__title span{color:var(--red)}
  .service__text{margin-top:3px;font-family:"Montserrat",sans-serif;font-size:7.4px;line-height:9.8px;color:#222;text-align:justify}
  .call-band{left:0;top:380px;width:430px;height:57px}
  .call-band__label{left:25px;top:384px;color:#fff;font-family:"Crimson Pro",serif;font-size:17px;letter-spacing:.5px;line-height:18px}
  .call-band__num{left:25px;top:397px;color:#fff;font-family:"Crimson Pro",serif;font-weight:700;font-size:29px;letter-spacing:.8px;line-height:34px}
  .mail-side{left:344px;top:0;width:312px;height:437px;
    background:radial-gradient(ellipse 130px 200px at 170px 260px,rgba(170,172,176,.55),rgba(170,172,176,0)),
      linear-gradient(160deg,#f7f7f8 0%,#e4e5e8 40%,#c9ccd1 100%)}
  .stamp{left:570px;top:35px;width:50px;height:58px;border:1.5px solid #666}
  .address-line{left:383px;width:235px;height:1px;background:var(--rule)}
</style>
</head>
<body>

<section class="postcard postcard--front" aria-label="Postcard front">
  <div class="abs hero" role="img" aria-label="Photo of a yellow two-storey house being pressure washed by a worker"></div>

  <svg class="abs promo-ribbon" viewBox="0 0 88 96" aria-hidden="true">
    <path d="M0 0H88V78L44 96L0 78Z" fill="#e11d27"/>
  </svg>
  <div class="abs promo-ribbon__text">
    <div class="promo-ribbon__amount">$25<small> off</small></div>
    <div class="promo-ribbon__sub">ANY SERVICE</div>
  </div>

  <h1 class="abs headline">PROFESSIONAL RESIDENTIAL &amp;<br>COMMERCIAL PRESSURE WASHING<br>CONTRACTOR IN ST. JOHNS COUNTY<br>AND SURROUNDING AREAS, FL</h1>

  <div class="abs result result--siding dirty" style="left:410px;top:7px" role="img" aria-label="Mildewed yellow siding before washing"><span class="result__label">BEFORE</span></div>
  <div class="abs result result--siding" style="left:532px;top:7px" role="img" aria-label="Clean yellow siding after washing"><span class="result__label">AFTER</span></div>
  <div class="abs result result--drive" style="left:410px;top:119px" role="img" aria-label="Stained concrete driveway before washing"><span class="result__label">BEFORE</span></div>
  <div class="abs result result--drive clean" style="left:532px;top:119px" role="img" aria-label="Clean concrete driveway after washing"><span class="result__label">AFTER</span></div>
  <div class="abs result result--porch" style="left:410px;top:230px" role="img" aria-label="Dirty porch ceiling before washing"><span class="result__label">BEFORE</span></div>
  <div class="abs result result--porch clean" style="left:532px;top:230px" role="img" aria-label="Clean porch ceiling after washing"><span class="result__label">AFTER</span></div>

  <div class="abs brand" style="left:32px;top:373px;font-size:18px">
    <span class="brand__mark" style="width:16px;height:16px"></span>Brightlane Wash Co.
  </div>

  <div class="abs call-box">
    <div class="call-box__top">CALL OR TEXT US NOW</div>
    <div class="call-box__num">555-014-2276</div>
  </div>
  <div class="abs contact" style="left:240px;top:386px;font-size:11.5px">
    <svg width="13" height="13" viewBox="0 0 14 14"><circle cx="7" cy="7" r="6.2" fill="none" stroke="#e11d27" stroke-width="1.1"/><rect x="4" y="4.8" width="6" height="4.4" fill="none" stroke="#555" stroke-width=".8"/><path d="M4 4.8L7 7.4L10 4.8" fill="none" stroke="#555" stroke-width=".8"/></svg>
    hello@brightlanewashco.com
  </div>
  <div class="abs contact" style="left:240px;top:404px;font-size:11.5px">
    <svg width="13" height="13" viewBox="0 0 14 14"><circle cx="7" cy="7" r="6.2" fill="none" stroke="#e11d27" stroke-width="1.1"/><circle cx="7" cy="7" r="3.6" fill="none" stroke="#555" stroke-width=".8"/><path d="M3.4 7H10.6M7 3.4V10.6" stroke="#555" stroke-width=".7"/></svg>
    www.brightlanewashco.com
  </div>

  <div class="abs pay-note" style="left:499px;top:345px;font-size:10.5px">All major credit card accepted</div>
  <div class="abs cards" style="left:494px;top:363px" aria-label="Accepted payment cards">
    <span class="card-chip chip-a"></span><span class="card-chip chip-b"></span><span class="card-chip chip-c"></span><span class="card-chip chip-d"></span>
  </div>
  <div class="abs social" style="left:522px;top:402px;font-size:10.5px">
    Follow us <span class="social__box" style="background:#3b5998"></span><span class="social__box" style="background:#c13584"></span>
  </div>
</section>

<section class="postcard postcard--back" aria-label="Postcard back">
  <div class="abs service-photo" role="img" aria-label="Photo of a worker pressure washing a grey house"></div>
  <div class="abs service-band"></div>

  <div class="abs thumb thumb--stain" style="left:15px" role="img" aria-label="Rust-stained wall base before"><span class="thumb__label">BEFORE</span></div>
  <div class="abs thumb thumb--wall" style="left:94px" role="img" aria-label="Clean wall base after"><span class="thumb__label">AFTER</span></div>
  <div class="abs thumb thumb--house" style="left:175px" role="img" aria-label="Grey house front before"><span class="thumb__label">BEFORE</span></div>
  <div class="abs thumb thumb--house clean" style="left:255px" role="img" aria-label="Grey house front after"><span class="thumb__label">AFTER</span></div>

  <h2 class="abs service-title">RESIDENTIAL PRESSURE WASHING</h2>
  <p class="abs service-sub">We offer pressure and soft washing services that allow us to protect your #1 investment.</p>

  <div class="abs services"></div>
  <div class="abs service" style="left:26px;top:236px;width:134px">
    <div class="service__title">HOUSE WASHING<br><span>ROOF CLEANING</span></div>
    <p class="service__text">We use a soft wash method that removes mildew, algae, mold, and other organic stains from the exterior of your house.</p>
  </div>
  <div class="abs service" style="left:181px;top:236px;width:148px">
    <div class="service__title">DRIVEWAY &amp;<br><span>CONCRETE CLEANING</span></div>
    <p class="service__text">Rejuvenate your property and remove dirt, grime, and other unwanted material with our expert exterior cleaning services.</p>
  </div>
  <div class="abs service" style="left:26px;top:313px;width:134px">
    <div class="service__title">GUTTER CLEANING<br><span>&amp; BRIGHTENING</span></div>
    <p class="service__text">Keep your gutters working correctly with a professional pressure washing service.</p>
  </div>
  <div class="abs service" style="left:181px;top:313px;width:148px">
    <div class="service__title">DECK &amp;<br><span>FENCE CLEANING</span></div>
    <p class="service__text">Rediscover outdoor living with professionally cleaned spaces.</p>
  </div>

  <div class="abs mail-side" role="img" aria-label="Faded photo of a worker in a company shirt pressure washing a house"></div>

  <svg class="abs call-band" viewBox="0 0 430 57" aria-hidden="true"><path d="M0 0H391L426 57H0Z" fill="#0f3f7f"/></svg>
  <div class="abs call-band__label">CALL OR TEXT US NOW</div>
  <div class="abs call-band__num">555-014-2276</div>
  <div class="abs contact" style="left:222px;top:389px;font-size:11px;color:#fff">
    <svg width="13" height="13" viewBox="0 0 14 14"><circle cx="7" cy="7" r="6.2" fill="none" stroke="#e11d27" stroke-width="1.1"/><rect x="4" y="4.8" width="6" height="4.4" fill="none" stroke="#fff" stroke-width=".8"/><path d="M4 4.8L7 7.4L10 4.8" fill="none" stroke="#fff" stroke-width=".8"/></svg>
    hello@brightlanewashco.com
  </div>
  <div class="abs contact" style="left:222px;top:409px;font-size:11px;color:#fff">
    <svg width="13" height="13" viewBox="0 0 14 14"><circle cx="7" cy="7" r="6.2" fill="none" stroke="#e11d27" stroke-width="1.1"/><circle cx="7" cy="7" r="3.6" fill="none" stroke="#fff" stroke-width=".8"/><path d="M3.4 7H10.6M7 3.4V10.6" stroke="#fff" stroke-width=".7"/></svg>
    www.brightlanewashco.com
  </div>

  <div class="abs brand" style="left:385px;top:56px;font-size:14px">
    <span class="brand__mark" style="width:11px;height:11px"></span>Brightlane Wash Co.
  </div>
  <div class="abs stamp"></div>
  <div class="abs address-line" style="top:167px"></div>
  <div class="abs address-line" style="top:203px"></div>
  <div class="abs address-line" style="top:241px"></div>

  <div class="abs pay-note" style="left:512px;top:367px;font-size:10.5px">All major credit card accepted</div>
  <div class="abs cards" style="left:494px;top:387px" aria-label="Accepted payment cards">
    <span class="card-chip chip-a"></span><span class="card-chip chip-b"></span><span class="card-chip chip-c"></span><span class="card-chip chip-d"></span>
  </div>
  <div class="abs social" style="left:565px;top:412px;font-size:10.5px">
    Follow us <span class="social__box" style="background:#3b5998"></span><span class="social__box" style="background:#c13584"></span>
  </div>
</section>

</body>
</html>
```